BEACON CABS

Taxi card design

Need changes very slow in replying to my messages.

Target Market(s)

Customers

Industry/Entity Type

Taxi

Contact Information for Business Card

See previous design

Font styles to use
Sans Serif

Colors
A7469A
B969AE
D3A5CF
EDDBEB
F8F0F9
6B429C
8869AF
B7A5CE
E3DAEB
F3F0F8

Requirements
Nice to have
• We are in the business of looking after people, not just driving vehicles front
Should not have
• Front number 01632 480 480 needs to big big

```html
<!DOCTYPE html>
<html lang="en">
<head>
<meta charset="utf-8">
<title>Beacon Cabs – Business Card</title>
<link href="https://fonts.googleapis.com/css2?family=Montserrat:wght@500;600;700;800&display=swap" rel="stylesheet">
<style>
  :root {
    --bg: #e6e6e6;
    --ink: #2b2b2b;
    --black: #050505;
    --white: #ffffff;
    --magenta: #a7469a;
    --magenta-light: #b969ae;
    --violet: #6b429c;
    --violet-mid: #8869af;
    --purple-grad: linear-gradient(180deg, #a7469a 0%, #6b429c 100%);
  }
  * { box-sizing: border-box; margin: 0; padding: 0; }
  html, body { width: 982px; height: 1200px; overflow: hidden; }
  body {
    background: var(--bg);
    font-family: "Montserrat", sans-serif;
    color: var(--ink);
    position: relative;
  }

  /* Brand lockup */
  .brand-lockup {
    position: absolute; left: 0; top: 48px; width: 982px;
    display: flex; flex-direction: column; align-items: center;
  }
  .brand-lockup .tagline { font-size: 26px; font-weight: 700; letter-spacing: 0.5px; color: var(--ink); margin-bottom: 10px; }
  .brand-name { display: flex; align-items: center; gap: 16px; }
  .brand-name .mark { width: 46px; height: 46px; background: var(--purple-grad); border-radius: 8px; }
  .brand-name .word { font-size: 68px; font-weight: 800; line-height: 1; letter-spacing: -1px; color: var(--ink); }
  .brand-lockup .since { font-size: 14px; font-weight: 600; color: var(--ink); margin-top: 8px; }

  /* Cards */
  .card {
    position: absolute; left: 141px; width: 700px; height: 398px; overflow: hidden;
    box-shadow: 0 6px 18px rgba(0,0,0,0.12);
  }
  .card-front { top: 240px; background: var(--white); }
  .card-back  { top: 682px; background: var(--black); }

  /* Front: header */
  .front-brand { position: absolute; left: 32px; top: 52px; }
  .front-brand .brand-name { gap: 10px; }
  .front-brand .mark { width: 28px; height: 28px; border-radius: 5px; }
  .front-brand .word { font-size: 40px; }
  .front-brand .since { font-size: 9px; font-weight: 700; margin: 4px 0 0 100px; }

  .service-tab {
    position: absolute; left: 414px; top: 62px; width: 286px; height: 60px;
    background: var(--black); border-radius: 12px 0 0 0;
    color: var(--white); font-size: 32px; font-weight: 700;
    display: flex; align-items: center; padding-left: 14px;
  }
  .service-tab-bar { position: absolute; left: 548px; top: 44px; width: 152px; height: 10px; background: var(--black); border-radius: 5px 0 0 0; }

  /* Front: black band */
  .info-band { position: absolute; left: 0; top: 146px; width: 700px; height: 150px; background: var(--black); }
  .services { position: absolute; left: 28px; top: 28px; list-style: none; }
  .services li {
    display: flex; align-items: center; gap: 12px;
    color: var(--white); font-size: 20px; font-weight: 600; letter-spacing: 3px;
    height: 34px;
  }
  .services li::before { content: ""; width: 15px; height: 15px; background: var(--magenta); }

  .phone-lines { position: absolute; left: 443px; top: 20px; }
  .phone-pill { position: relative; display: flex; align-items: center; height: 28px; margin-bottom: 12px; }
  .phone-pill .pill {
    display: flex; align-items: center; gap: 10px;
    width: 182px; height: 26px; padding-left: 10px;
    background: linear-gradient(90deg, var(--violet) 0%, var(--magenta) 100%);
    border-radius: 12px 2px 12px 2px;
    color: var(--white); font-size: 14px; font-weight: 700; letter-spacing: 1.5px;
  }
  .phone-pill .speed { margin-left: 4px; }

  /* Front: footer */
  .contact { position: absolute; left: 34px; top: 308px; font-size: 15px; font-weight: 500; line-height: 21px; color: var(--black); }
  .address { position: absolute; left: 480px; top: 308px; font-size: 15px; font-weight: 500; line-height: 21px; color: var(--black); }

  /* Back */
  .back-wave { position: absolute; left: 0; top: 0; }
  .back-brand { position: absolute; left: 0; top: 138px; width: 700px; display: flex; justify-content: center; }
  .back-brand .mark { width: 40px; height: 40px; }
  .back-brand .word { font-size: 58px; color: var(--white); }
  .back-phone {
    position: absolute; left: 0; top: 296px; width: 700px;
    display: flex; justify-content: center; align-items: center; gap: 12px;
    color: var(--white); font-size: 34px; font-weight: 700; letter-spacing: 5px;
  }
</style>
</head>
<body>

  <header class="brand-lockup">
    <p class="tagline">24/7 SERVICE</p>
    <div class="brand-name"><span class="mark"></span><span class="word">Beacon Cabs</span></div>
    <p class="since">Established since 1986</p>
  </header>

  <section class="card card-front" aria-label="Business card front">
    <div class="front-brand">
      <div class="brand-name"><span class="mark"></span><span class="word">Beacon Cabs</span></div>
      <p class="since">Established since 1986</p>
    </div>
    <div class="service-tab-bar"></div>
    <div class="service-tab">24/7 SERVICE</div>

    <div class="info-band">
      <ul class="services">
        <li>AIRPORT TRANSFERS</li>
        <li>MINIBUSES</li>
        <li>SCHOOL TRANSPORT</li>
      </ul>
      <div class="phone-lines">
        <div class="phone-pill">
          <span class="pill">
            <svg width="10" height="14" viewBox="0 0 10 14"><rect x="1" y="0.5" width="8" height="13" rx="1.5" fill="none" stroke="#fff" stroke-width="1.2"/><circle cx="5" cy="11" r="0.9" fill="#fff"/></svg>
            01632 480 111
          </span>
          <svg class="speed" width="30" height="24" viewBox="0 0 30 24"><rect x="0" y="2" width="22" height="3" fill="#6b429c"/><rect x="6" y="8" width="24" height="3" fill="#8869af"/><rect x="2" y="14" width="18" height="3" fill="#6b429c"/><rect x="10" y="20" width="12" height="3" fill="#8869af"/></svg>
        </div>
        <div class="phone-pill">
          <span class="pill">
            <svg width="10" height="14" viewBox="0 0 10 14"><rect x="1" y="0.5" width="8" height="13" rx="1.5" fill="none" stroke="#fff" stroke-width="1.2"/><circle cx="5" cy="11" r="0.9" fill="#fff"/></svg>
            01632 480 222
          </span>
          <svg class="speed" width="30" height="24" viewBox="0 0 30 24"><rect x="0" y="2" width="22" height="3" fill="#6b429c"/><rect x="6" y="8" width="24" height="3" fill="#8869af"/><rect x="2" y="14" width="18" height="3" fill="#6b429c"/><rect x="10" y="20" width="12" height="3" fill="#8869af"/></svg>
        </div>
        <div class="phone-pill">
          <span class="pill">
            <svg width="10" height="14" viewBox="0 0 10 14"><rect x="1" y="0.5" width="8" height="13" rx="1.5" fill="none" stroke="#fff" stroke-width="1.2"/><circle cx="5" cy="11" r="0.9" fill="#fff"/></svg>
            01632 480 333
          </span>
          <svg class="speed" width="30" height="24" viewBox="0 0 30 24"><rect x="0" y="2" width="22" height="3" fill="#6b429c"/><rect x="6" y="8" width="24" height="3" fill="#8869af"/><rect x="2" y="14" width="18" height="3" fill="#6b429c"/><rect x="10" y="20" width="12" height="3" fill="#8869af"/></svg>
        </div>
      </div>
    </div>

    <p class="contact">Freephone: 0800 555 0 123<br>E-mail: hello@beaconcabs.example<br>Website: www.beaconcabs.example</p>
    <p class="address">St Marys Parish Hall<br>Market Street Ashford<br>AB1 2CD</p>
  </section>

  <section class="card card-back" aria-label="Business card back">
    <svg class="back-wave" width="700" height="398" viewBox="0 0 700 398">
      <defs>
        <linearGradient id="backPurple" x1="0" y1="0" x2="0" y2="1">
          <stop offset="0" stop-color="#8869af"/>
          <stop offset="1" stop-color="#6b429c"/>
        </linearGradient>
      </defs>
      <path d="M0,236 Q350,300 700,230 L700,398 L0,398 Z" fill="url(#backPurple)"/>
    </svg>
    <div class="back-brand">
      <div class="brand-name"><span class="mark"></span><span class="word">Beacon Cabs</span></div>
    </div>
    <div class="back-phone">
      <svg width="26" height="30" viewBox="0 0 26 30"><rect width="26" height="30" rx="4" fill="#050505"/><rect x="8" y="6" width="10" height="17" rx="1.5" fill="none" stroke="#fff" stroke-width="1.4"/><circle cx="13" cy="20" r="1" fill="#fff"/></svg>
      <span>01632 480 480</span>
    </div>
  </section>

</body>
</html>
```